Book Cover 2d & 3d for Brontel Leafpad

I need a book cover created in both 2d & 3d for Brontel Leafpad and general marketing purposes.
Title: Multiply Your Revenue: A Quick Message Drafting Sprint
Subtitle: Discover Ways to Compose Simple Notes for Top Budget Customers
Author: Dustin Halvorsen
See attachment for example cover design I like.
I will provide further copy to complete the back cover with exerpts from the book.

```html
<!DOCTYPE html>
<html lang="en">
<head>
<meta charset="utf-8">
<title>Multiply Your Revenue — Book Cover</title>
<link href="https://fonts.googleapis.com/css2?family=Anton&family=Arimo:wght@400;700&display=swap" rel="stylesheet">
<style>
  :root {
    --page-bg: #f4f1ec;
    --cover-coral: #f2605a;
    --cover-peach: #fde9da;
    --wave-orange: #f7874f;
    --wave-soft: #f9a06a;
    --ink: #161616;
    --accent-red: #e8302c;
    --band-white: #f4f4f6;
    --art-navy: #27336e;
    --art-blue: #3d4fa0;
  }
  * { margin: 0; padding: 0; box-sizing: border-box; }
  html, body { width: 1200px; height: 960px; overflow: hidden; }
  body { background: var(--page-bg); position: relative; }

  .book-cover {
    position: absolute; left: 280px; top: 40px;
    width: 640px; height: 880px; overflow: hidden;
    background: linear-gradient(180deg, var(--cover-peach) 0%, #f9b79a 20%, var(--cover-coral) 42%, var(--cover-coral) 100%);
  }
  .cover-waves { position: absolute; inset: 0; }

  .cover-art {
    position: absolute; left: 140px; top: 18px; width: 290px; height: 290px;
    border-radius: 22px;
    background: linear-gradient(160deg, var(--art-navy) 0%, var(--art-blue) 60%, #ffffff 100%);
  }

  .cover-title {
    position: absolute; left: 150px; top: 232px;
    font-family: "Anton", sans-serif; color: var(--ink);
    line-height: 1.02; letter-spacing: 0.5px; text-transform: uppercase;
  }
  .cover-title .line-main { display: block; font-size: 34px; }
  .cover-title .line-accent { display: block; font-size: 32px; color: var(--accent-red); padding-left: 70px; }
  .cover-title .line-tail { display: block; font-size: 30px; padding-left: 6px; }

  .subtitle-band {
    position: absolute; left: 120px; top: 548px; width: 500px; height: 72px;
    background: var(--band-white);
    display: flex; align-items: center; justify-content: center;
    font-family: "Arimo", sans-serif; font-size: 21px; line-height: 1.2;
    color: var(--ink); text-align: center;
  }

  .author-name {
    position: absolute; left: 120px; width: 480px; top: 808px;
    font-family: "Arimo", sans-serif; font-size: 19px; color: var(--ink);
    text-align: center;
  }
  .author-rule {
    position: absolute; left: 110px; width: 500px; top: 836px; height: 2px;
    background: #ffffff;
  }
</style>
</head>
<body>
  <main class="book-cover">
    <svg class="cover-waves" width="640" height="880" viewBox="0 0 640 880" aria-hidden="true">
      <path d="M0 230 C120 170 200 300 330 250 C460 200 540 300 640 250 L640 0 L0 0 Z" fill="var(--wave-soft)" opacity="0.35"/>
      <path d="M110 330 C200 290 300 360 420 320 C500 290 560 330 640 300 L640 380 C540 410 470 360 380 390 C280 420 200 370 110 390 Z" fill="var(--wave-orange)" opacity="0.55"/>
      <path d="M480 0 C470 40 520 60 500 110" stroke="var(--wave-orange)" stroke-width="16" fill="none" stroke-linecap="round" opacity="0.6"/>
    </svg>

    <div class="cover-art" role="img" aria-label="Illustration of an open envelope with a letter on a dark blue background"></div>

    <h1 class="cover-title">
      <span class="line-main">Multiply Your Revenue:</span>
      <span class="line-accent">A Quick</span>
      <span class="line-tail">Message Drafting Sprint</span>
    </h1>

    <p class="subtitle-band">Discover Ways to Compose Simple Notes<br>for Top Budget Customers</p>

    <p class="author-name">Dustin Halvorsen</p>
    <div class="author-rule"></div>
  </main>
</body>
</html>
```